Fast Money - Simple Book Cover Design

Hello,

I am in need of a cover for my new book. The Book Title Is

"Standing Growth - Keys to Glowing Customer Ratings That Fill The Calendar and Draw Fresh Clients Through Every Entrance!"

Author: Fireman Dale Orsworth

What I want: This is a book for businesses on improving their online reputation. I want to have 5 Stars on the cover. You can look at this quarvex search for ideas of what I am meaning.....

(copy and paste)

http://www.quarvex-find.example/search?q=5+star+online+reviews&mode=images&ref=kx7Lp2QwZt9 (copy and paste)

I am open to different color schemes for the book. I am partial to dark blues if you make it look good. Here is another book that I really like the cover of....

http://www.brindlemart.example/Clipwave-Tactics-Earning-Promotion-ebook/item/Z93KT4WQPX

I want the cover BOLD and to STAND OUT.

I am looking for a design to help establish me as an authority for online reputation marketing. This book will be both in Pagely format and be used in print as well.

I am open to questions....

Thanks!

Dale

Reason: I don't believe we have received the right designs. I am going to give everyone more time...

Reason: Hi everyone, I had some stuff come up and was not able to be involved in this project. I am extending because we have not seen the exact thing we want and need time to work with designers to get it right. Thanks Dale

Reason: I am currently traveling and can't wrap this up until I get back.

Target Market(s)

Business Owners

Industry/Entity Type

Business

Requirements
Must have
• Title and Subtitle

Author Name

5 Stars Images....
Nice to have
• Creativity

Bold and stand out

Professional

Should not have
• thin text, small to read text, lame graphics,

```html
<!DOCTYPE html>
<html lang="en">
<head>
<meta charset="utf-8">
<title>Standing Growth – Book Cover</title>
<link href="https://fonts.googleapis.com/css2?family=Arimo:wght@700&family=Share+Tech+Mono&display=swap" rel="stylesheet">
<style>
  :root {
    --navy-deep: #1f2560;
    --navy-top: #232a68;
    --band-title: #2c3574;
    --band-title-low: #323b7c;
    --band-subtitle: #3b4589;
    --band-author: #8b91c4;
    --bar-dark: #3a4080;
    --star-fill: #8e94c6;
    --star-edge: #ffffff;
    --star-glow: #4a66ff;
    --rule: #e8eaf6;
    --ink-light: #ffffff;
    --ink-dark: #1c2258;
    --icon: #dadff2;
  }
  * { margin: 0; padding: 0; box-sizing: border-box; }
  html, body { width: 1200px; height: 1200px; overflow: hidden; background: var(--navy-deep); }
  .cover {
    position: relative;
    width: 1200px;
    height: 1200px;
    overflow: hidden;
    background: var(--navy-deep);
  }
  .band { position: absolute; left: 0; width: 100%; }
  .band--top { top: 0; height: 200px; background: var(--navy-top); }
  .band--title { top: 200px; height: 200px; background: var(--band-title); }
  .band--title-low { top: 400px; height: 203px; background: var(--band-title-low); }
  .band--subtitle { top: 603px; height: 194px; background: var(--band-subtitle); }
  .band--author { top: 797px; height: 203px; background: var(--band-author); }
  .rule { position: absolute; left: 0; width: 100%; height: 3px; background: var(--rule); }
  .rule--upper { top: 601px; }
  .rule--lower { top: 796px; }
  .author-bar { position: absolute; top: 907px; height: 53px; background: var(--bar-dark); }
  .author-bar--left { left: 0; width: 529px; }
  .author-bar--right { left: 1129px; width: 71px; }
  .stars { position: absolute; inset: 0; width: 1200px; height: 1200px; }
  .title {
    position: absolute;
    top: 252px;
    left: 0;
    width: 100%;
    text-align: center;
    font-family: "Arimo", Arial, sans-serif;
    font-weight: 700;
    font-size: 120px;
    letter-spacing: -1px;
    color: var(--ink-light);
    text-shadow: 4px 5px 6px rgba(10, 12, 40, 0.85);
    line-height: 1;
  }
  .subtitle {
    position: absolute;
    top: 614px;
    left: 100px;
    font-family: "Share Tech Mono", "Courier New", monospace;
    font-size: 40px;
    line-height: 58px;
    letter-spacing: 5px;
    color: var(--ink-light);
    text-shadow: 2px 3px 3px rgba(10, 12, 40, 0.8);
    white-space: nowrap;
  }
  .author {
    position: absolute;
    top: 905px;
    left: 560px;
    font-family: "Arimo", Arial, sans-serif;
    font-weight: 700;
    color: var(--ink-dark);
    line-height: 56px;
    white-space: nowrap;
  }
  .author__by { font-size: 30px; margin-right: 16px; }
  .author__name { font-size: 40px; letter-spacing: 1px; }
  .phone-icon { position: absolute; left: 1015px; top: 682px; width: 170px; height: 200px; }
</style>
</head>
<body>
<main class="cover">
  <div class="band band--top"></div>
  <div class="band band--title"></div>
  <div class="band band--title-low"></div>
  <div class="band band--subtitle"></div>
  <div class="band band--author"></div>
  <div class="rule rule--upper"></div>
  <div class="rule rule--lower"></div>
  <div class="author-bar author-bar--left"></div>
  <div class="author-bar author-bar--right"></div>

  <svg class="stars" viewBox="0 0 1200 1200" aria-hidden="true">
    <defs>
      <filter id="star-glow" x="-30%" y="-30%" width="160%" height="160%">
        <feGaussianBlur in="SourceAlpha" stdDeviation="9" result="blur"/>
        <feFlood flood-color="#4a66ff"/>
        <feComposite in2="blur" operator="in" result="glow"/>
        <feMerge><feMergeNode in="glow"/><feMergeNode in="glow"/><feMergeNode in="SourceGraphic"/></feMerge>
      </filter>
      <polygon id="hexagram" points="0,-1 0.2887,-0.5 0.866,-0.5 0.5774,0 0.866,0.5 0.2887,0.5 0,1 -0.2887,0.5 -0.866,0.5 -0.5774,0 -0.866,-0.5 -0.2887,-0.5"/>
    </defs>
    <g filter="url(#star-glow)" fill="var(--star-fill)" stroke="var(--star-edge)">
      <use href="#hexagram" transform="translate(215 118) rotate(12) scale(118)" stroke-width="0.05"/>
      <use href="#hexagram" transform="translate(440 487) rotate(8) scale(92)" stroke-width="0.065"/>
      <use href="#hexagram" transform="translate(700 487) rotate(4) scale(88)" stroke-width="0.07"/>
      <use href="#hexagram" transform="translate(900 495) rotate(8) scale(68)" stroke-width="0.085"/>
      <use href="#hexagram" transform="translate(1048 460) rotate(4) scale(48)" stroke-width="0.115"/>
    </g>
  </svg>

  <h1 class="title">Standing&nbsp; Growth</h1>

  <p class="subtitle">Keys to Glowing Customer Ratings That<br>Fill The Calendar &amp; Draw Fresh<br>Clients Through Every Entrance!</p>

  <svg class="phone-icon" viewBox="0 0 180 210" aria-hidden="true">
    <path d="M40 20 C25 22 12 40 18 70 C26 110 60 150 95 165 C110 172 122 166 128 156 L112 136 C106 140 98 142 90 136 C70 120 56 100 50 78 C48 68 52 60 58 56 Z" fill="var(--icon)"/>
    <path d="M62 16 l18 22 -14 10 -18 -22 Z M132 150 l-18 -22 14 -10 18 22 Z" fill="var(--icon)"/>
    <path d="M108 40 a18 18 0 0 1 14 14 M112 26 a32 32 0 0 1 24 24 M116 12 a46 46 0 0 1 34 34" fill="none" stroke="var(--icon)" stroke-width="5" stroke-linecap="round"/>
    <path d="M130 160 c8 10 4 22 12 26 c8 4 10 -8 18 -4 c8 4 2 14 10 18" fill="none" stroke="var(--icon)" stroke-width="5" stroke-linecap="round"/>
  </svg>

  <p class="author"><span class="author__by">by</span><span class="author__name">Fireman&nbsp; Dale&nbsp; Orsworth</span></p>
</main>
</body>
</html>
```